Elegant wine label

Looking for a new Napa Valley wine label called "Velmira". Our wines will retail for $150 + per bottle. Velmira is derived from the greek word Ergo (therefore) tied in with Air for aeration for wine.

We handcraft our small production wine. 200 cases.
Looking for a very sophisticated, minimalist elegant look. Wine labels we like for inspiration and reference include: www.trelk.wine, www.plavicwine.com, www.morvinestates.com, www.dunleafywine.com, www.kretavine.com/Wine, https://shop.gavrelwine.com/wine

Colors will include white, black and blue foil (Approx. color: C 94.9, M 83.53, Y 0, K 0). We want a custom-created, minimal greek/roman looking font for lettering.

```html
<!DOCTYPE html>
<html lang="en">
<head>
<meta charset="utf-8">
<title>Velmira — Wine Label</title>
<link rel="stylesheet" href="https://fonts.googleapis.com/css2?family=Italiana&display=swap">
<style>
  :root {
    --backdrop: #dcdce4;
    --label-black: #0b0b10;
    --label-ink: #14151f;
    --foil-blue: #0d2aff;
    --foil-blue-deep: #1a2a9c;
    --type-white: #f6f6f8;
    --edge-shadow: rgba(20, 20, 35, 0.22);
  }

  * { margin: 0; padding: 0; box-sizing: border-box; }

  html, body {
    width: 1200px;
    height: 1198px;
    overflow: hidden;
    background: var(--backdrop);
  }

  .canvas {
    position: relative;
    width: 1200px;
    height: 1198px;
    display: flex;
    align-items: center;
    justify-content: center;
  }

  .wine-label {
    position: relative;
    width: 900px;
    height: 600px;
    display: flex;
    align-items: center;
    justify-content: center;
    background:
      radial-gradient(ellipse 65% 55% at 50% 20%, rgba(13, 42, 255, 0.38) 0%, rgba(13, 42, 255, 0) 70%),
      radial-gradient(ellipse 60% 45% at 85% 100%, rgba(26, 42, 156, 0.35) 0%, rgba(26, 42, 156, 0) 70%),
      linear-gradient(180deg, var(--label-ink) 0%, var(--label-black) 100%);
    box-shadow: 0 20px 50px var(--edge-shadow);
  }

  .wine-label__name {
    font-family: "Italiana", "Didot", serif;
    font-weight: 400;
    font-size: 170px;
    letter-spacing: 2px;
    color: var(--type-white);
    line-height: 1;
    white-space: nowrap;
  }
</style>
</head>
<body>
  <main class="canvas">
    <section class="wine-label" aria-label="Velmira wine label">
      <h1 class="wine-label__name">Velmira</h1>
    </section>
  </main>
</body>
</html>
```